HARBOURLINE FORGE GYM FLYER DESIGN

We want a flyer designed for our gym. We have an example of a flyer which we like and I have put it into the images I have uploaded. I would like to recreate using our pictures, so its a pretty straight forward job. We also want to put our weekly timetable on the back of the flyer. We would like the size of the flyer to be A5.

Target Market(s)

FITNESS

Industry/Entity Type

Gym

Colors
33a6d7
ffffff

Requirements
Must have
• We just want to recreate the flyer but we must have the following info on the flyer and we want our timetable on the back of the flyer which you can get from this link: http://www.harbourlineforgegym.com/timetable
• Harbourline Forge Gym is a fun community of humble people. Our goal is to help guide you towards a fitter, healthier lifestyle!
• Our Programs
• HIIT
• High intensity interval training is 30-45 minutes of fat burning fun. The class is a mix of cardio, bodyweight and some resistance movements.
• Conditioning
• A full hour of strength, cardio and bodyweight training to get you in tip top shape. Expect a mix of barbells, kettlebells, rowing machines, bikes and other training methods.
• QMP
• This is our big Friday session to set you up for the weekend. 90 minutes of hard training that is done with a team emphasis. From heavy lifting to cardio triathlons, this class has it all but not for the faint hearted.
• Muay Thai
• Commonly known as the science of 8 limbs you will learn how to punch, kick, knee and elbow. Thailands national sport is a great way to get your fitness kick. We train the complete beginner all the way to international fighters so you are in great hands.
• Kids Muay Thai
• Our junior program starts from age 6 onwards. Muay Thai is a great way for kids to get active and fit while learning new skills. Training in martial arts also teaches self discipline and socialisation skills.
• Yoga
• A combination of physical and mental practises that will leave you focused and refreshed for whatever the week throws at you. We always recommend our yoga classes as a great way to balance the high intensity training we offer.
• Q-Move
• Strength training with a little bit of conditioning. We regularly update the program and re test lifts to ensure you are making progress and getting stronger.
• CONTACT US
• OUR LOCATION:
• Unit 27C
• 214 Caskin Street
• Wester Holm
• Glasgow
• G72LT
• Phone: 07392615084
• Email: info@harbourlineforgegym.com
• Web: www.harbourlineforgegym.com
Nice to have
• Can use all the picture but if not be good to use the boxing one and the group training one.

```html
<!DOCTYPE html>
<html lang="en">
<head>
<meta charset="utf-8">
<title>Harbourline Forge Gym – A5 Flyer</title>
<link rel="stylesheet" href="https://fonts.googleapis.com/css2?family=Bebas+Neue&family=PT+Sans+Narrow:wght@700&family=Questrial&display=swap">
<style>
:root{
  --brand:#1ba9e6;
  --brand-deep:#1697d2;
  --brand-band:#1ea2dd;
  --stripe:#1590cc;
  --white:#ffffff;
  --ink:#111111;
  --label:#7a7a7a;
  --photo-dark:#2b2f2c;
}
*{box-sizing:border-box;margin:0;padding:0}
html,body{width:1200px;height:1200px;overflow:hidden;background:var(--white)}
body{position:relative;font-family:"Questrial",sans-serif;color:var(--ink)}
.sheet-title{position:absolute;left:83px;top:34px;font-size:34px;color:var(--label)}
.side-label{position:absolute;font-size:36px;color:var(--ink)}
.side-label.front{left:214px;top:186px}
.side-label.back{left:212px;top:780px}

.flyer{position:absolute;left:335px;width:756px;height:533px;overflow:hidden;background:var(--brand);color:var(--white)}
.flyer.front{top:90px}
.flyer.back{top:652px}
.flyer svg.backdrop{position:absolute;left:0;top:0}
.abs{position:absolute}

.brand-name{font-family:"Bebas Neue",sans-serif;font-size:21px;letter-spacing:1px;width:248px;text-align:center;top:24px;left:0}
.intro{left:27px;top:89px;width:215px;font-size:13.4px;line-height:15.3px}
.join{left:0;width:248px;top:196px;text-align:center;font-family:"Bebas Neue",sans-serif;font-size:23px;display:flex;align-items:center;justify-content:center;gap:8px}
.join::before,.join::after{content:"";width:36px;height:1px;background:var(--white)}
.join-web{left:44px;top:222px;font-family:"PT Sans Narrow",sans-serif;font-size:10px}

.programs-title{left:270px;top:253px;font-family:"Bebas Neue",sans-serif;font-size:23px}
.program{position:absolute;width:212px}
.program h3{font-family:"Bebas Neue",sans-serif;font-weight:400;font-size:22px;line-height:22px;margin-bottom:2px}
.program p{font-family:"PT Sans Narrow",sans-serif;font-size:8.4px;line-height:10.6px}
.contact{left:24px;right:22px;top:506px;border-top:1px solid var(--white);padding-top:6px;font-family:"PT Sans Narrow",sans-serif;font-size:9.6px;display:flex}
.contact .lead{font-family:"Bebas Neue",sans-serif;font-size:12px;width:100px}
.contact span.sep{margin:0 12px}

.gym-address{left:34px;top:84px;font-size:13px;line-height:15.5px}
.gym-address .name{display:block;margin-bottom:16px}
.timetable-title{left:65px;top:183px;font-family:"Bebas Neue",sans-serif;font-size:24px}
.timetable{position:absolute;left:0;top:218px;width:750px;border-collapse:collapse;font-family:"PT Sans Narrow",sans-serif;font-size:10.6px}
.timetable th{font-family:"Bebas Neue",sans-serif;font-weight:400;font-size:22px;height:29px;border-left:1px solid var(--white);border-top:1px solid var(--white)}
.timetable th:first-child{border-left:none}
.timetable td{height:16.5px;padding:0 6px;border-left:1px solid var(--white);white-space:nowrap;line-height:16.5px}
.timetable td.time{padding-left:12px;border-left:none}
.timetable tbody tr:nth-child(odd){background:var(--stripe)}
</style>
</head>
<body>
<div class="sheet-title">A5 Gym Flyer</div>
<div class="side-label front">front</div>
<div class="side-label back">back</div>

<section class="flyer front">
  <svg class="backdrop" width="756" height="533" viewBox="0 0 756 533">
    <rect width="756" height="533" fill="var(--brand)"/>
    <polygon points="0,58 118,66 130,74 248,70 248,172 130,176 118,182 0,172" fill="var(--brand-band)"/>
    <rect x="248" y="0" width="508" height="270" fill="var(--photo-dark)" role="img" aria-label="Photo: group kettlebell training class in the gym"/>
    <defs>
      <linearGradient id="groupPhoto" x1="0" y1="0" x2="1" y2="1">
        <stop offset="0" stop-color="#3a3d3a"/><stop offset=".55" stop-color="#2a2e2a"/><stop offset="1" stop-color="#3d5a3a"/>
      </linearGradient>
      <linearGradient id="boxingPhoto" x1="0" y1="0" x2="1" y2="1">
        <stop offset="0" stop-color="#5a4b48"/><stop offset=".5" stop-color="#8a6e62"/><stop offset="1" stop-color="#b8353a"/>
      </linearGradient>
    </defs>
    <rect x="248" y="0" width="508" height="270" fill="url(#groupPhoto)"/>
    <polygon points="0,265 248,246 248,533 0,533" fill="url(#boxingPhoto)" role="img" aria-label="Photo: woman boxing on pads in the ring"/>
    <polygon points="248,246 756,206 756,533 248,533" fill="var(--brand)"/>
    <line x1="281" y1="300" x2="281" y2="440" stroke="var(--white)" stroke-width="1"/>
    <line x1="521" y1="248" x2="521" y2="447" stroke="var(--white)" stroke-width="1"/>
    <g fill="var(--white)">
      <circle cx="281" cy="297" r="11"/><circle cx="281" cy="361" r="11"/><circle cx="281" cy="434" r="11"/>
      <circle cx="521" cy="246" r="11"/><circle cx="521" cy="320" r="11"/><circle cx="521" cy="385" r="11"/><circle cx="521" cy="444" r="11"/>
    </g>
    <g fill="none" stroke="var(--brand)" stroke-width="2">
      <circle cx="281" cy="297" r="6"/><path d="M281 293v4l3 2"/>
      <circle cx="281" cy="362" r="5"/><path d="M278 356h6"/>
      <path d="M275 434h12M277 430v8M285 430v8"/>
      <path d="M517 250l4-8 4 8M521 242v-3"/>
      <path d="M521 315v10M517 325h8"/>
      <path d="M515 389l6-8 6 8z"/>
      <path d="M515 444h12M517 440v8M525 440v8"/>
    </g>
  </svg>

  <div class="abs brand-name">Harbourline Forge Gym</div>
  <p class="abs intro">Harbourline Forge Gym is a fun community of humble people. Our goal is to help guide you towards a fitter, healthier lifestyle!</p>
  <div class="abs join">Join Today!</div>
  <div class="abs join-web">www.harbourlineforgegym.com</div>

  <h2 class="abs programs-title" style="font-weight:400">Our Programs</h2>
  <div class="program" style="left:303px;top:286px">
    <h3>HIIT</h3>
    <p>High intensity interval training is 30-45 minutes of fat burning fun. The class is a mix of cardio, bodyweight and some resistance movements.</p>
  </div>
  <div class="program" style="left:303px;top:350px">
    <h3>Conditioning</h3>
    <p>A full hour of strength, cardio and bodyweight training to get you in tip top shape. Expect a mix of barbells, kettlebells, rowing machines, bikes and other training methods.</p>
  </div>
  <div class="program" style="left:303px;top:423px">
    <h3>QMP</h3>
    <p>This is our big Friday session to set you up for the weekend. 90 minutes of hard training that is done with a team emphasis. From heavy lifting to cardio triathlons, this class has it all but not for the faint hearted.</p>
  </div>
  <div class="program" style="left:544px;top:235px">
    <h3>Muay Thai</h3>
    <p>Commonly known as the science of 8 limbs you will learn how to punch, kick, knee and elbow. We train the complete beginner all the way to international fighters so you are in great hands.</p>
  </div>
  <div class="program" style="left:544px;top:309px">
    <h3>Kids Muay Thai</h3>
    <p>Our junior program starts from age 6 onwards. Kids to get active and fit while learning new skills. It also teaches self discipline and socialisation skills.</p>
  </div>
  <div class="program" style="left:544px;top:374px">
    <h3>Yoga</h3>
    <p>A combination of physical and mental that will leave you focused and refreshed. Our yoga classes complements the high intensity training we offer.</p>
  </div>
  <div class="program" style="left:544px;top:433px">
    <h3>Q-Move</h3>
    <p>Strength training with a little bit of conditioning. We regularly update the program and re test lifts to ensure you are making progress and getting stronger.</p>
  </div>

  <div class="abs contact">
    <span class="lead">Contact us:</span>
    <span>07392615084</span><span class="sep">|</span>
    <span>info@harbourlineforgegym.com</span><span class="sep">|</span>
    <span>www.harbourlineforgegym.com</span>
  </div>
</section>

<section class="flyer back">
  <svg class="backdrop" width="756" height="533" viewBox="0 0 756 533">
    <defs>
      <linearGradient id="kettlebellPhoto" x1="0" y1="0" x2="1" y2="1">
        <stop offset="0" stop-color="#2e3340"/><stop offset=".5" stop-color="#3f6d3a"/><stop offset="1" stop-color="#3b2f2a"/>
      </linearGradient>
      <linearGradient id="jumpPhoto" x1="0" y1="0" x2="1" y2="1">
        <stop offset="0" stop-color="#2a2a2a"/><stop offset=".5" stop-color="#7d8580"/><stop offset="1" stop-color="#4a4f4e"/>
      </linearGradient>
    </defs>
    <rect width="756" height="533" fill="var(--brand)"/>
    <polygon points="0,70 118,70 130,77 248,70 248,176 130,176 118,182 0,176" fill="var(--brand-band)"/>
    <rect x="248" y="0" width="258" height="176" fill="url(#kettlebellPhoto)" role="img" aria-label="Photo: man swinging a kettlebell"/>
    <rect x="509" y="0" width="247" height="176" fill="url(#jumpPhoto)" role="img" aria-label="Photo: woman performing a jumping exercise"/>
    <line x1="0" y1="218" x2="756" y2="218" stroke="var(--white)" stroke-width="1"/>
  </svg>

  <div class="abs brand-name">Harbourline Forge Gym</div>
  <p class="abs gym-address"><span class="name">HARBOURLINE FORGE GYM</span>Unit 27C, 214 Caskin Street<br>Wester Holm , Glasgow&nbsp; G72LT</p>
  <h2 class="abs timetable-title" style="font-weight:400">Our Timetable</h2>

  <table class="timetable">
    <colgroup>
      <col style="width:52px"><col style="width:118px"><col style="width:118px"><col style="width:118px"><col style="width:119px"><col style="width:115px"><col style="width:110px">
    </colgroup>
    <thead>
      <tr><th></th><th>Mon</th><th>Tue</th><th>Wed</th><th>Thu</th><th>Fri</th><th>Sat</th></tr>
    </thead>
    <tbody>
      <tr><td class="time">06:00</td><td></td><td>Q-Move</td><td>Strength &amp; Conditioning</td><td></td><td>Q-Move</td><td></td></tr>
      <tr><td class="time">07:00</td><td>Conditioning</td><td>Fight Camp Muay Thai</td><td>Yoga</td><td>Conditioning</td><td>Fight Camp Muay Thai</td><td></td></tr>
      <tr><td class="time">08:00</td><td>Open Gym</td><td>Open Gym</td><td>Open Gym</td><td>Open Gym</td><td>Open Gym</td><td></td></tr>
      <tr><td class="time">10:00</td><td>Q-Move</td><td></td><td>Q-Move</td><td></td><td>Q-Move</td><td>Saturday Circuit</td></tr>
      <tr><td class="time">11:00</td><td></td><td></td><td></td><td></td><td></td><td>Open Gym</td></tr>
      <tr><td class="time">11:00</td><td></td><td></td><td></td><td></td><td></td><td>Fundamentals</td></tr>
      <tr><td class="time">11:00</td><td></td><td></td><td></td><td></td><td></td><td>Kids</td></tr>
      <tr><td class="time">12:00</td><td></td><td></td><td></td><td></td><td></td><td>Muay Thai Foundation</td></tr>
      <tr><td class="time">12:10</td><td>Lunch Time HIIT</td><td>Lunch Time HIIT</td><td></td><td>Lunch Time HIIT</td><td>Lunch Time HIIT</td><td></td></tr>
      <tr><td class="time">16:00</td><td>Open Gym</td><td>Open Gym</td><td>Open Gym</td><td>Open Gym</td><td>Open Gym</td><td></td></tr>
      <tr><td class="time">17:00</td><td>Q-Move</td><td></td><td>Q-Move</td><td></td><td>Q-Move</td><td></td></tr>
      <tr><td class="time">17:15</td><td></td><td>HIIT</td><td>HIIT</td><td>HIIT</td><td></td><td></td></tr>
      <tr><td class="time">18:00</td><td>Fundamentals</td><td>Conditioning</td><td>Fundamentals</td><td>Conditioning</td><td>QMP</td><td></td></tr>
      <tr><td class="time">18:00</td><td>Muay Thai Foundation</td><td>Kids</td><td>Muay Thai Foundation</td><td>Kids</td><td></td><td></td></tr>
      <tr><td class="time">19:00</td><td>Strength &amp; Conditioning</td><td>Muay Thai Intermediate</td><td></td><td>Muay Thai Intermediate</td><td></td><td></td></tr>
      <tr><td class="time">19:15</td><td></td><td></td><td>Yoga</td><td></td><td></td><td></td></tr>
    </tbody>
  </table>
</section>
</body>
</html>
```